Commercial HVAC and Refrigeration Business cards

Frost-Line Company is looking for flashy new business cards! We design, install, service and maintain commercial refrigeration, air conditioning, heating and refrigeration equipment. Our colors are blue and white. I'm open to single and double sided designs. Each employee will have their own business card. I've attached a copy of our current logo.

Our website, office and cell phone (cell phone is optional), email address should be clearly legible. "24 Hour Service" and the services we offer are; Sales, Service, Design, Installation, Maintenance. Refrigeration, Heating, Air Conditioning, Ice Machines. Does not have to be in any order.

Target Market(s)

Commercial; Restaurants, hotels, bars, breweries etc.

Industry/Entity Type

Hvac

Contact Information for Business Card

Name; Job Title, Phone Number, Email Address. www.frost-line-example.com 24 Hour Service. We provide - Sales, Design, Installation, Service, Maintenance. We service - Refrigeration, Heating, Air Conditioning, Ice Machines

Font styles to use
Other font styles liked:
• Be creative

Colors
0255a3
ffffff

Requirements
Must have
• Professional appearance and appeal to commercial clients in the food-service and hospitality industry. Must be clearly legible and easy to understand.
Nice to have
• We want to sell maintenance agreements, perhaps we can use the back of the card to tie into a webpage about our maintenance agreements.
Should not have
• Cartoons or unprofessional. Nothing too edgy.

```html
<!DOCTYPE html>
<html lang="en">
<head>
<meta charset="utf-8">
<title>Frost-Line Company – Business Cards</title>
<link href="https://fonts.googleapis.com/css2?family=Open+Sans:ital,wght@0,400;0,600;0,700;1,700&display=swap" rel="stylesheet">
<style>
  :root {
    --brand-blue: #0255a3;
    --brand-blue-dark: #024485;
    --white: #ffffff;
    --ink-grey: #6b6f75;
    --rule-grey: #c9ccd1;
    --canvas-bg: #ecedef;
  }
  * { box-sizing: border-box; margin: 0; padding: 0; }
  html, body {
    width: 1200px; height: 950px; overflow: hidden;
    background: var(--canvas-bg);
    font-family: "Open Sans", Arial, sans-serif;
  }
  .card {
    position: absolute;
    width: 620px; height: 354px;
    border-radius: 4px;
    box-shadow: 0 10px 28px rgba(0,0,0,.18);
    overflow: hidden;
  }

  /* Back side */
  .card-back {
    left: 90px; top: 80px;
    background: var(--brand-blue);
    color: var(--white);
  }
  .card-back .wordmark {
    position: absolute; top: 70px; left: 0; right: 0;
    text-align: center;
    font-size: 44px; font-weight: 600; letter-spacing: .5px;
    color: var(--white);
  }
  .offer-heading {
    position: absolute; top: 178px; left: 40px; right: 40px;
    display: flex; align-items: center; gap: 14px;
    font-size: 19px; font-weight: 700;
  }
  .offer-heading::before, .offer-heading::after {
    content: ""; flex: 1; height: 1px; background: rgba(255,255,255,.75);
  }
  .service-list {
    position: absolute; top: 222px; left: 46px; right: 30px;
    font-size: 15.5px; line-height: 28px;
  }
  .service-list .label { display: inline-block; width: 100px; font-size: 17px; }

  /* Front side */
  .card-front {
    left: 490px; top: 500px;
    background: var(--white);
  }
  .card-front .wordmark {
    position: absolute; top: 62px; left: 120px;
    font-size: 40px; font-weight: 600;
    color: var(--brand-blue);
  }
  .person {
    position: absolute; top: 196px; left: 150px; width: 140px;
    text-align: right;
  }
  .person .name { font-size: 21px; font-weight: 600; color: var(--brand-blue); }
  .person .title { font-size: 16px; color: var(--ink-grey); margin-top: 2px; }
  .divider {
    position: absolute; left: 310px; top: 172px; width: 1px; height: 86px;
    background: var(--rule-grey);
  }
  .contacts {
    position: absolute; top: 170px; left: 330px;
    list-style: none; font-size: 15.5px; color: var(--ink-grey);
  }
  .contacts li { display: flex; align-items: center; gap: 10px; height: 29px; }
  .contacts svg { width: 17px; height: 17px; fill: var(--brand-blue); flex: none; }
  .bottom-band { position: absolute; left: 0; bottom: 0; width: 620px; height: 72px; }
  .service-tag {
    position: absolute; right: 40px; bottom: 36px;
    height: 28px; line-height: 28px;
    font-size: 16px; font-weight: 700; font-style: italic; color: var(--white);
  }
</style>
</head>
<body>

<section class="card card-back" aria-label="Business card back">
  <div class="wordmark">Frost-Line Company</div>
  <div class="offer-heading">Maintenance agreements</div>
  <div class="service-list">
    <div><span class="label">We provide :</span> Sales | Design | Installation | Service | Maintenance</div>
    <div><span class="label">We service :</span> Refrigeration | Heating | Air Conditioning | Ice Machines</div>
  </div>
</section>

<section class="card card-front" aria-label="Business card front">
  <div class="wordmark">Frost-Line Company</div>

  <div class="person">
    <div class="name">Mark Ellison</div>
    <div class="title">President</div>
  </div>
  <div class="divider"></div>

  <ul class="contacts">
    <li>
      <svg viewBox="0 0 24 24" aria-hidden="true"><path d="M6.6 10.8a15.1 15.1 0 0 0 6.6 6.6l2.2-2.2a1 1 0 0 1 1-.25 11.4 11.4 0 0 0 3.6.57 1 1 0 0 1 1 1V20a1 1 0 0 1-1 1A17 17 0 0 1 3 4a1 1 0 0 1 1-1h3.5a1 1 0 0 1 1 1c0 1.25.2 2.45.57 3.6a1 1 0 0 1-.25 1z"/></svg>
      555 014 2538
    </li>
    <li>
      <svg viewBox="0 0 24 24" aria-hidden="true"><path d="M2 5h20v14H2z M2 5l10 8 10-8" fill="none" stroke="#0255a3" stroke-width="2"/><path d="M3 5h18l-9 7z"/></svg>
      john@frost-line-example.com
    </li>
    <li>
      <svg viewBox="0 0 24 24" aria-hidden="true"><circle cx="12" cy="12" r="9" fill="none" stroke="#0255a3" stroke-width="2"/><path d="M3 12h18M12 3c3 3 3 15 0 18M12 3c-3 3-3 15 0 18" fill="none" stroke="#0255a3" stroke-width="1.6"/></svg>
      www.frost-line-example.com
    </li>
  </ul>

  <svg class="bottom-band" viewBox="0 0 620 72" aria-hidden="true">
    <rect x="0" y="40" width="620" height="2" fill="var(--rule-grey)"/>
    <rect x="0" y="44" width="620" height="28" fill="var(--brand-blue)"/>
    <polygon points="352,6 620,6 620,72 326,72" fill="var(--brand-blue-dark)"/>
  </svg>
  <div class="service-tag">24 Hour Service.</div>
</section>

</body>
</html>
```